Brackenridge Strength Studio Chronic Pain Flyer

Double sided DL flyer required to promote a strength training studio to sufferers of chronic pain. Flyer will be displayed in osteopathy, chiropractic and massage clinics. Flyer should be clean, professional and appeal to an older (40+) demographic.

Target Market(s)

Chronic pain sufferers. Age 40+

Industry/Entity Type

Health And Wellness

Colors

Designer to choose colors to be used in the design.

Requirements
Must have
• See attached files for text copy and logo. Image(s) of people strength training with a coach or personal trainer, as well as images depicting pain in common parts of the body (such as those pictured in the supplied mock up)
• website address: brackenridgestrengthstudio.example.com.au
• phone number : 0452 918 304
• Street address: 4/63 Juniper Hollow Rd, Brackenridge
Nice to have
• Images such as in the attached files.

```html
<!DOCTYPE html>
<html lang="en">
<head>
<meta charset="utf-8">
<title>Brackenridge Strength Studio – DL Flyer</title>
<link href="https://fonts.googleapis.com/css2?family=Lato:ital,wght@0,300;0,400;0,700;0,900;1,300;1,900&display=swap" rel="stylesheet">
<style>
  :root{
    --red:#e31b23;
    --red-deep:#a50f14;
    --red-dark:#5e0d10;
    --ink:#232323;
    --paper:#efefeb;
    --stage:#e4e6e9;
    --rule:#c9c9c4;
    --white:#ffffff;
  }
  *{box-sizing:border-box;margin:0;padding:0}
  html,body{width:1200px;height:1200px;overflow:hidden}
  body{background:var(--stage);font-family:'Lato',Arial,sans-serif;color:var(--ink);position:relative}
  .flyer{position:absolute;top:207px;width:440px;height:785px;background:var(--paper);overflow:hidden;box-shadow:0 6px 18px rgba(0,0,0,.18)}
  .flyer--front{left:100px}
  .flyer--back{left:660px}
  .flyer__art{position:absolute;inset:0}
  .brand{position:absolute;top:38px;right:46px;font-weight:900;font-size:13px;letter-spacing:.5px;color:var(--red-deep);text-transform:uppercase;display:flex;align-items:center;gap:6px}
  .brand__dot{width:9px;height:9px;border-radius:50%;background:var(--red-deep)}
  .headline{position:absolute;right:42px;text-align:right;line-height:1}
  .headline--front{top:418px}
  .headline__line{font-size:48px;font-weight:400;color:var(--ink);display:block;margin-bottom:8px}
  .headline__accent{font-size:60px;font-weight:900;color:var(--red);display:block;margin-top:10px}
  .divider{position:absolute;left:84px;right:60px;top:628px;height:1px;background:var(--rule)}
  .contact{position:absolute;left:0;right:0;text-align:center}
  .contact--front{top:648px}
  .contact__phone{font-size:30px;font-weight:900;font-style:italic;display:flex;align-items:center;justify-content:center;gap:6px}
  .contact__line{font-size:18px;font-weight:300;display:flex;align-items:center;justify-content:center;gap:6px;margin-top:6px}
  .contact__line--web,.contact__line--addr{font-style:italic}
  .icon{width:18px;height:18px;flex:none}
  .back-title{position:absolute;right:52px;top:38px;text-align:right}
  .back-title__kicker{font-size:17px;font-weight:400;letter-spacing:.3px}
  .back-title__main{font-size:36px;font-weight:900;color:var(--red);line-height:1.15}
  .tagline{position:absolute;right:40px;top:126px;text-align:right;font-size:31px;font-weight:300;line-height:40px}
  .copy{position:absolute;left:46px;right:38px;top:362px;font-size:11.6px;line-height:16.5px;font-weight:400;color:#333}
  .copy p+p{margin-top:13px}
  .contact--back{top:652px;color:var(--white)}
  .contact--back .contact__phone{font-style:normal}
</style>
</head>
<body>

<section class="flyer flyer--front" aria-label="Flyer front">
  <svg class="flyer__art" viewBox="0 0 440 785" width="440" height="785">
    <defs>
      <linearGradient id="gymPhoto" x1="0" y1="0" x2="1" y2="1">
        <stop offset="0" stop-color="#bcd3e6"/>
        <stop offset=".5" stop-color="#e8ddd6"/>
        <stop offset="1" stop-color="#d9a0ad"/>
      </linearGradient>
      <linearGradient id="frontWave" x1="0" y1="0" x2="1" y2="0">
        <stop offset="0" stop-color="#8e0c10"/>
        <stop offset=".6" stop-color="#c8141a"/>
        <stop offset="1" stop-color="#a50f14"/>
      </linearGradient>
    </defs>
    <path d="M0 250 C60 150 150 60 260 80 C340 95 390 110 440 90 L440 260 C360 270 300 300 230 335 C160 370 80 385 0 390 Z" fill="url(#gymPhoto)" role="img" aria-label="Photo: a coach guiding a smiling woman lifting a barbell in a gym"/>
    <path d="M30 185 C90 90 170 50 260 68 C340 84 390 100 440 70 L440 92 C390 118 340 104 262 86 C180 70 100 110 30 185 Z" fill="#1d1d1d"/>
    <path d="M0 390 C80 385 160 370 230 335 C300 300 360 270 440 250 L440 320 C380 330 320 350 260 385 C180 435 90 462 0 470 Z" fill="url(#frontWave)"/>
  </svg>
  <div class="brand"><span class="brand__dot"></span>Brackenridge Strength Studio</div>
  <h1 class="headline headline--front">
    <span class="headline__line">HEALTH</span>
    <span class="headline__line">THROUGH</span>
    <span class="headline__accent">STRENGTH</span>
  </h1>
  <div class="divider"></div>
  <div class="contact contact--front">
    <div class="contact__phone">
      <svg class="icon" viewBox="0 0 24 24"><path d="M6.6 10.8a15 15 0 0 0 6.6 6.6l2.2-2.2a1 1 0 0 1 1-.25 11.4 11.4 0 0 0 3.6.57 1 1 0 0 1 1 1V20a1 1 0 0 1-1 1A17 17 0 0 1 3 4a1 1 0 0 1 1-1h3.5a1 1 0 0 1 1 1c0 1.250.2 2.450.57 3.57a1 1 0 0 1-.25 1z" fill="currentColor"/></svg>
      0452 918 304
    </div>
    <div class="contact__line contact__line--web">
      <svg class="icon" viewBox="0 0 24 24" fill="none" stroke="currentColor" stroke-width="1.6"><circle cx="12" cy="12" r="9"/><path d="M3 12h18M12 3c3 3 3 15 0 18M12 3c-3 3-3 15 0 18"/></svg>
      brackenridgestrengthstudio.example.com.au
    </div>
    <div class="contact__line contact__line--addr">
      <svg class="icon" viewBox="0 0 24 24" fill="none" stroke="currentColor" stroke-width="1.8"><path d="M12 21s-6-6.2-6-11a6 6 0 0 1 12 0c0 4.8-6 11-6 11z"/><circle cx="12" cy="10" r="2.2"/></svg>
      4/63 Juniper Hollow Rd, Brackenridge
    </div>
  </div>
</section>

<section class="flyer flyer--back" aria-label="Flyer back">
  <svg class="flyer__art" viewBox="0 0 440 785" width="440" height="785">
    <defs>
      <linearGradient id="painPhoto" x1="0" y1="0" x2="1" y2="0">
        <stop offset="0" stop-color="#c4c4c2"/>
        <stop offset=".6" stop-color="#dcdcd9"/>
        <stop offset="1" stop-color="#efefeb"/>
      </linearGradient>
      <linearGradient id="backBand" x1="0" y1="0" x2="0" y2="1">
        <stop offset="0" stop-color="#d0161c"/>
        <stop offset=".55" stop-color="#9d1015"/>
        <stop offset="1" stop-color="#4f0c0e"/>
      </linearGradient>
      <linearGradient id="circleA" x1="0" y1="0" x2="1" y2="1"><stop offset="0" stop-color="#d4d4d2"/><stop offset="1" stop-color="#b8b8b6"/></linearGradient>
      <linearGradient id="circleB" x1="0" y1="0" x2="1" y2="1"><stop offset="0" stop-color="#8d8f93"/><stop offset="1" stop-color="#d6d6d6"/></linearGradient>
      <linearGradient id="circleC" x1="0" y1="0" x2="1" y2="1"><stop offset="0" stop-color="#c2cdd6"/><stop offset="1" stop-color="#d8d8d6"/></linearGradient>
    </defs>
    <rect x="0" y="0" width="280" height="340" fill="url(#painPhoto)" role="img" aria-label="Photo: woman seen from behind holding her shoulder and lower back in pain"/>
    <path d="M0 340 C110 300 300 292 440 340 L440 355 C300 320 120 320 0 355 Z" fill="var(--red)"/>
    <path d="M0 640 C60 590 120 570 220 570 C320 570 380 590 440 640 L440 785 L0 785 Z" fill="#d2d2cf"/>
    <path d="M0 650 C60 600 120 582 220 582 C320 582 380 600 440 650 L440 785 L0 785 Z" fill="url(#backBand)"/>
    <circle cx="122" cy="585" r="58" fill="url(#circleA)" stroke="#efefeb" stroke-width="3" role="img" aria-label="Photo: hand holding a painful knee"/>
    <circle cx="220" cy="565" r="60" fill="url(#circleB)" stroke="#efefeb" stroke-width="3" role="img" aria-label="Photo: trainer coaching a woman with a dumbbell"/>
    <circle cx="318" cy="585" r="58" fill="url(#circleC)" stroke="#efefeb" stroke-width="3" role="img" aria-label="Photo: hand holding a painful shoulder"/>
  </svg>
  <div class="back-title">
    <div class="back-title__kicker">HEALTH THROUGH</div>
    <div class="back-title__main">STRENGTH</div>
  </div>
  <div class="tagline">You don’t<br>have<br>to live<br>in pain.</div>
  <div class="copy">
    <p>Strength training has been shown to improve many chronic pain conditions and is now being routinely recommended by medical and health professionals.</p>
    <p>Our private studio provides high quality strength training by expert strength coaches. We’ve helped countless people improve or eliminate chronic pain, contact us today and find out how we can help you.</p>
  </div>
  <div class="contact contact--back">
    <div class="contact__phone">
      <svg class="icon" viewBox="0 0 24 24"><path d="M6.6 10.8a15 15 0 0 0 6.6 6.6l2.2-2.2a1 1 0 0 1 1-.25 11.4 11.4 0 0 0 3.6.57 1 1 0 0 1 1 1V20a1 1 0 0 1-1 1A17 17 0 0 1 3 4a1 1 0 0 1 1-1h3.5a1 1 0 0 1 1 1c0 1.250.2 2.450.57 3.57a1 1 0 0 1-.25 1z" fill="currentColor"/></svg>
      0452 918 304
    </div>
    <div class="contact__line">
      <svg class="icon" viewBox="0 0 24 24" fill="none" stroke="currentColor" stroke-width="1.6"><circle cx="12" cy="12" r="9"/><path d="M3 12h18M12 3c3 3 3 15 0 18M12 3c-3 3-3 15 0 18"/></svg>
      brackenridgestrengthstudio.example.com.au
    </div>
    <div class="contact__line">
      <svg class="icon" viewBox="0 0 24 24" fill="none" stroke="currentColor" stroke-width="1.8"><path d="M12 21s-6-6.2-6-11a6 6 0 0 1 12 0c0 4.8-6 11-6 11z"/><circle cx="12" cy="10" r="2.2"/></svg>
      4/63 Juniper Hollow Rd, Brackenridge
    </div>
  </div>
</section>

</body>
</html>
```